Corvale Holdings Business Cards

Hello. I need business cards designed with our new logo. I'd like to see at least 3 different designs. At least one with a dark background, and at least one with a white background. Maybe one with gray or blue for the background. Play with gradient colors and maybe even insert a pic of a skyline in the background of one or more of them. Use your judgement. We will need 2 cards printed. They need to accommodate the employee name, title, company address, phone, email, and website. Thanks.

Target Market(s)

Wealthy mature investors.

Contact Information for Business Card

Single-sided, professional, clean design that incorporates our logo.

Font styles to use
Sans Serif

Requirements
Must have
• Our new logo needs to be featured on it. (See attached.)
• Employee Name (In all CAPS)
• Title
• Street Address, City, ST Zip Code
• Cell Phone #, Email Address, Website Address
Nice to have
• Design that blends well with our new logo and its colors, or a city scape or other graphic design that looks like an apartment complex in the background. Blues and grays are nice, but use your judgement.
Should not have
• Modern or oriental looking designs or bright colors.

```html
<!DOCTYPE html>
<html lang="en">
<head>
<meta charset="utf-8">
<title>Corvale Holdings Business Cards</title>
<link href="https://fonts.googleapis.com/css2?family=Montserrat:wght@500&family=Open+Sans:wght@400;600&display=swap" rel="stylesheet">
<style>
  :root {
    --backdrop: #1c1c1e;
    --card: #121315;
    --accent: #2fa9e4;
    --text-muted: #8b8e93;
    --text-soft: #a3a6ab;
  }
  * { margin: 0; padding: 0; box-sizing: border-box; }
  html, body {
    width: 1200px; height: 900px; overflow: hidden;
    background: var(--backdrop);
  }
  .canvas { position: relative; width: 1200px; height: 900px; }

  .card {
    position: absolute;
    width: 640px; height: 366px;
    background: var(--card);
    border-radius: 22px;
    box-shadow: 0 12px 30px rgba(0,0,0,0.45);
  }
  .card--front { left: 400px; top: 40px; }
  .card--back  { left: 160px; top: 480px; }

  .wordmark {
    font-family: "Montserrat", sans-serif;
    font-weight: 500;
    color: var(--accent);
    text-transform: uppercase;
    line-height: 1;
  }
  .wordmark__line { display: block; }

  .card--front .wordmark {
    position: absolute; left: 0; right: 0; top: 140px;
    text-align: center;
  }
  .card--front .wordmark__name { font-size: 46px; letter-spacing: 2px; }
  .card--front .wordmark__sub  { font-size: 19px; letter-spacing: 3px; margin-top: 8px; }

  .card--back .wordmark {
    position: absolute; left: 52px; top: 150px;
  }
  .card--back .wordmark__name { font-size: 31px; letter-spacing: 1.5px; }
  .card--back .wordmark__sub  { font-size: 13px; letter-spacing: 2px; margin-top: 6px; }

  .divider {
    position: absolute; left: 330px; top: 90px;
    width: 2px; height: 180px;
    background: var(--accent);
  }

  .contact {
    position: absolute; left: 358px; top: 92px;
    font-family: "Open Sans", sans-serif;
  }
  .contact__name {
    font-size: 25px; color: var(--text-muted); font-weight: 400;
    letter-spacing: 0.5px; line-height: 1;
  }
  .contact__name strong { font-weight: 600; }
  .contact__title {
    font-size: 15px; color: var(--accent); margin-top: 6px;
  }
  .contact__list { list-style: none; margin-top: 18px; }
  .contact__item {
    display: flex; align-items: center; gap: 9px;
    font-size: 16px; color: var(--text-soft);
    height: 22px;
  }
  .contact__icon { width: 15px; height: 15px; flex: none; }
  .contact__address {
    font-size: 16px; color: var(--text-muted); margin-top: 14px;
  }
</style>
</head>
<body>
<main class="canvas">

  <section class="card card--front" aria-label="Card front">
    <div class="wordmark">
      <span class="wordmark__line wordmark__name">Corvale</span>
      <span class="wordmark__line wordmark__sub">Holdings, LLC</span>
    </div>
  </section>

  <section class="card card--back" aria-label="Card back">
    <div class="wordmark">
      <span class="wordmark__line wordmark__name">Corvale</span>
      <span class="wordmark__line wordmark__sub">Holdings, LLC</span>
    </div>

    <div class="divider"></div>

    <div class="contact">
      <p class="contact__name">YOUR <strong>NAME</strong></p>
      <p class="contact__title">CA LIC/ #482906</p>
      <ul class="contact__list">
        <li class="contact__item">
          <svg class="contact__icon" viewBox="0 0 16 16" aria-hidden="true">
            <path fill="var(--accent)" d="M2 5c0-1.5 2.5-2.5 6-2.5S14 3.5 14 5v1.2h-3V5H5v1.2H2z"/>
            <rect x="3" y="7" width="10" height="7" rx="1.2" fill="var(--accent)"/>
            <circle cx="8" cy="10.5" r="1.6" fill="var(--card)"/>
          </svg>
          000 000 0000
        </li>
        <li class="contact__item">
          <svg class="contact__icon" viewBox="0 0 16 16" aria-hidden="true">
            <rect x="1.5" y="3.5" width="13" height="9" rx="1" fill="var(--accent)"/>
            <path d="M2 4.2l6 4.6 6-4.6" fill="none" stroke="var(--card)" stroke-width="1.3"/>
          </svg>
          youremail@xyz.com
        </li>
        <li class="contact__item">
          <svg class="contact__icon" viewBox="0 0 16 16" aria-hidden="true">
            <g fill="none" stroke="var(--text-soft)" stroke-width="1.1">
              <circle cx="8" cy="8" r="6.3"/>
              <ellipse cx="8" cy="8" rx="2.8" ry="6.3"/>
              <path d="M1.7 8h12.6M2.7 4.8h10.6M2.7 11.2h10.6"/>
            </g>
          </svg>
          www.yourwebsite.com
        </li>
      </ul>
      <p class="contact__address">Street Address, City, ST Zip Code</p>
    </div>
  </section>

</main>
</body>
</html>
```